Brindle Capital and Investments

Create a simple business card design using the logos attached. Make it similar but not exact to the reference photo. Brand guidelines are also included.

```html
<!DOCTYPE html>
<html lang="en">
<head>
<meta charset="utf-8">
<title>Brindle Capital — Business Card</title>
<link href="https://fonts.googleapis.com/css2?family=Montserrat:wght@400;500;700&display=swap" rel="stylesheet">
<style>
  :root {
    --backdrop: #2a2a2c;
    --navy: #1f2640;
    --navy-light: #4a536c;
    --copper: #b4581f;
    --white: #ffffff;
  }
  * { margin: 0; padding: 0; box-sizing: border-box; }
  html, body {
    width: 1200px; height: 875px; overflow: hidden;
    background: var(--backdrop);
    font-family: "Montserrat", sans-serif;
  }
  .canvas {
    width: 1200px; height: 875px;
    display: flex; align-items: center; justify-content: center; gap: 40px;
  }
  .card {
    position: relative;
    width: 540px; height: 309px;
    background: var(--navy);
    border-bottom: 4px solid var(--copper);
    overflow: hidden;
  }
  .card--front {
    background: linear-gradient(100deg, var(--navy-light) 0%, #3a4360 22%, var(--navy) 42%);
    display: flex; align-items: center; justify-content: center;
  }
  .wordmark {
    color: var(--white);
    font-weight: 700;
    letter-spacing: 0.08em;
    text-transform: uppercase;
    display: flex; align-items: center; gap: 12px;
  }
  .wordmark__dot {
    width: 12px; height: 12px; border-radius: 50%;
    background: var(--white);
  }
  .card--front .wordmark { font-size: 34px; }
  .card--back { border-left: 4px solid var(--copper); }
  .person {
    position: absolute; top: 46px; right: 40px;
    text-align: right;
  }
  .person__name {
    color: var(--copper);
    font-weight: 700; font-size: 22px;
    letter-spacing: 0.01em; text-transform: uppercase;
  }
  .person__role {
    color: var(--white);
    font-size: 13px; margin-top: 3px;
  }
  .person__bar {
    position: absolute; top: 46px; right: 22px;
    width: 8px; height: 46px; background: var(--copper);
  }
  .details {
    position: absolute; left: 36px; bottom: 30px;
    color: var(--white);
  }
  .card--back .wordmark { font-size: 20px; margin-bottom: 14px; }
  .card--back .wordmark__dot { width: 9px; height: 9px; }
  .address { font-size: 12px; line-height: 1.5; margin-bottom: 12px; }
  .contact-list { list-style: none; font-size: 12px; line-height: 1.6; }
  .contact-list li { display: flex; align-items: center; gap: 8px; }
  .contact-list svg { width: 12px; height: 12px; fill: var(--copper); flex: none; }
</style>
</head>
<body>
<main class="canvas">
  <section class="card card--front" aria-label="Card front">
    <div class="wordmark"><span class="wordmark__dot"></span>Brindle Capital</div>
  </section>

  <section class="card card--back" aria-label="Card back">
    <div class="person">
      <p class="person__name">Maren Whitlock</p>
      <p class="person__role">Managing Director</p>
    </div>
    <span class="person__bar"></span>

    <div class="details">
      <div class="wordmark"><span class="wordmark__dot"></span>Brindle Capital</div>
      <p class="address">Your address, City<br>State, Zip 1234</p>
      <ul class="contact-list">
        <li><svg viewBox="0 0 24 24"><path d="M6.6 10.8a15.1 15.1 0 0 0 6.6 6.6l2.2-2.2c.3-.3.7-.4 1-.2 1.1.4 2.3.6 3.6.6.6 0 1 .4 1 1V20c0 .6-.4 1-1 1A17 17 0 0 1 3 4c0-.6.4-1 1-1h3.5c.6 0 1 .4 1 1 0 1.3.2 2.5.6 3.6.1.3 0 .7-.2 1z"/></svg>123 456 789</li>
        <li><svg viewBox="0 0 24 24"><path d="M7 1h10a2 2 0 0 1 2 2v18a2 2 0 0 1-2 2H7a2 2 0 0 1-2-2V3a2 2 0 0 1 2-2zm0 3v15h10V4zm5 16a1 1 0 1 0 0 2 1 1 0 0 0 0-2z"/></svg>123 456 789</li>
        <li><svg viewBox="0 0 24 24"><path d="M2 5h20v14H2zm2 2v.5l8 5 8-5V7zm0 2.8V17h16V9.8l-8 5z"/></svg>info@brindlecapital.com</li>
        <li><svg viewBox="0 0 24 24"><path d="M12 2a10 10 0 1 0 0 20 10 10 0 0 0 0-20zm6.9 6h-3a15 15 0 0 0-1.3-3.9A8 8 0 0 1 18.9 8zM12 4c.8 1.2 1.5 2.5 1.9 4h-3.8c.4-1.5 1.1-2.8 1.9-4zM4.3 14a8 8 0 0 1 0-4h3.4a16 16 0 0 0 0 4zm.8 2h3a15 15 0 0 0 1.3 3.9A8 8 0 0 1 5.1 16zm3-8h-3a8 8 0 0 1 4.3-3.9C8.8 5.3 8.4 6.6 8.1 8zM12 20c-.8-1.2-1.5-2.5-1.9-4h3.8c-.4 1.5-1.1 2.8-1.9 4zm2.3-6H9.7a14 14 0 0 1 0-4h4.6a14 14 0 0 1 0 4zm.3 5.9c.6-1.2 1-2.5 1.3-3.9h3a8 8 0 0 1-4.3 3.9zm1.7-5.9a16 16 0 0 0 0-4h3.4a8 8 0 0 1 0 4z"/></svg>www.brindlecapital.com</li>
      </ul>
    </div>
  </section>
</main>
</body>
</html>
```